Flyer-Design für Touristikportal
Zielgruppe
Wir sind ein Online Reise- und Touristikportal: www.wegfalke.de mit einer Auswahl und Vielfalt an Reisen, die es sonst nicht gibt. Unsere Zielgruppe sind alle reiseaffinen Personen im Alter von 25 - 80 Jahren.
Aufgabenstellung
Der DIN Lang Flyer MUSS ein Eyecatcher sein bzw. haben. Nichts standardmäßiges, nichts langweiliges, nicht billig wirkend. Man muß sofort erkennen um was es geht - Reisen, Touren, Aktivitäten. Evtl. ein knackiger Slogan, ein Bild, das Emotionen weckt? Der DIN Lang Flyer liegt in Geschäften, Apotheken etc. aus - er muß ansprechend wirken! Auf der Rückseite sollte stehen, was wir alles anbieten, jetzt nicht im Detail, aber einen guten Überblick!

```html
<!DOCTYPE html>
<html lang="de">
<head>
<meta charset="utf-8">
<title>Wegfalke – Flyer DIN lang, Fensterfalz</title>
<link href="https://fonts.googleapis.com/css2?family=Lato:wght@400;700;900&display=swap" rel="stylesheet">
<style>
  :root{
    --paper:#ffffff;
    --ink:#3a3a3a;
    --body:#333333;
    --teal:#4fb3ae;
    --white:#ffffff;
    --frame:#9a9a9a;
    --sunset: linear-gradient(180deg,#8e86c4 0%,#c79ac6 22%,#f0b58a 42%,#e8c7a0 50%,#6fbcc0 62%,#3fa3ad 100%);
    --sunset-warm: linear-gradient(180deg,#d9a3c8 0%,#f2b68e 30%,#f5c99a 42%,#8ec3bf 58%,#4aa7b0 100%);
    --lilac: linear-gradient(180deg,#8f8ad2 0%,#b39ad8 30%,#9a7fb8 52%,#c7a6d8 70%,#e2c6e6 100%);
  }
  *{box-sizing:border-box;margin:0;padding:0}
  html,body{width:1200px;height:1000px;overflow:hidden;background:var(--paper)}
  body{position:relative;font-family:"Lato",sans-serif;color:var(--ink)}

  .spread{position:absolute;left:36px;width:1127px;height:282px;outline:1px solid var(--frame)}
  .spread--outside{top:36px}
  .spread--inside{top:333px}

  .photo{position:absolute;top:0;height:100%}
  .photo--jetty{background:var(--sunset)}
  .photo--jetty-warm{background:var(--sunset-warm)}
  .photo--clouds{background:var(--lilac)}

  .panel{position:absolute;top:0;height:100%}
  .panel--left{left:0;width:279px}
  .panel--mid{left:279px;width:570px;background:var(--paper)}
  .panel--right{left:849px;width:278px}

  .headline{position:absolute;color:var(--white);font-weight:900;font-size:47px;line-height:44px;letter-spacing:-1px;text-transform:uppercase;white-space:nowrap}

  .brand-name{position:absolute;left:0;width:100%;text-align:center;font-size:28px;font-weight:400;letter-spacing:0.5px;color:var(--ink);line-height:1}

  .contact{position:absolute;left:0;width:100%;text-align:center;color:var(--ink)}
  .contact__phone{font-size:12px;font-weight:700;letter-spacing:0.3px}
  .contact__hours{font-size:7.5px;margin-top:1px}
  .contact__mail{font-size:12px;font-weight:700;margin-top:7px}

  .inside-curve{position:absolute;left:0;top:0}

  .intro{position:absolute;left:230px;width:666px;top:104px;text-align:center}
  .intro__lead{color:var(--teal);font-weight:700;font-size:12px;letter-spacing:0.3px}
  .intro__text{font-size:9.4px;line-height:14.3px;letter-spacing:0.25px;color:var(--body);margin-top:12px}
  .intro__claim{font-size:9.4px;letter-spacing:0.25px;color:var(--body);margin-top:11px}
  .intro__claim b{font-weight:700}

  .offer{position:absolute;left:0;top:0;width:100%;height:100%;list-style:none}
  .offer__item{position:absolute;display:flex;align-items:center}
  .offer__icon{width:29px;height:29px;border-radius:50%;background:var(--teal);border:1.5px solid #e9f6f5;display:flex;align-items:center;justify-content:center;flex:none}
  .offer__label{position:absolute;left:913px;color:var(--white);font-size:17px;font-weight:700;letter-spacing:1.2px;white-space:nowrap}

  .closed{position:absolute;left:36px;top:654px;width:556px;height:283px;box-shadow:5px 5px 6px rgba(0,0,0,0.35)}
  .closed__fold{position:absolute;left:279px;top:0;width:1px;height:100%;background:rgba(255,255,255,0.25)}

  .note{position:absolute;left:657px;top:773px;font-size:18px;line-height:22px;color:#1a1a1a}
</style>
</head>
<body>

<!-- Außenseite -->
<section class="spread spread--outside">
  <div class="panel panel--left photo photo--jetty" role="img" aria-label="Foto: Holzsteg zu Wasserbungalows über türkisem Meer in der Abenddämmerung"></div>

  <div class="panel panel--mid">
    <div class="brand-name" style="top:46px">WEGFALKE</div>
    <div class="contact" style="top:214px">
      <div class="contact__phone">+49 30 / 5550 412 0</div>
      <div class="contact__hours">(Mo – Sa von 07.00 bis 20.00)</div>
      <div class="contact__mail">info@wegfalke.de</div>
    </div>
  </div>

  <div class="panel panel--right photo photo--jetty-warm" role="img" aria-label="Foto: Wasserbungalows und Steg im Sonnenuntergang">
    <h2 class="headline" style="left:26px;top:54px">Wir sind<br>voller<br>Reise-<br>vielfalt</h2>
  </div>
</section>

<!-- Innenseite -->
<section class="spread spread--inside">
  <div class="photo photo--clouds" style="left:0;width:300px" role="img" aria-label="Foto: Vulkanlandschaft über einem Wolkenmeer in lila Dämmerung"></div>
  <div class="photo photo--clouds" style="left:827px;width:300px" role="img" aria-label="Foto: Berggipfel über Wolken im violetten Abendlicht"></div>

  <svg class="inside-curve" width="1127" height="282" viewBox="0 0 1127 282" aria-hidden="true">
    <path d="M277 0 L849 0 Q913 141 849 282 L277 282 Q213 141 277 0 Z" fill="#ffffff"/>
  </svg>

  <h2 class="headline" style="left:30px;top:64px">Wir sind<br>Weg-<br>Falke</h2>

  <div class="brand-name" style="top:46px">WEGFALKE</div>

  <div class="intro">
    <p class="intro__lead">Komm mit uns dem Himmel einfach etwas näher – nicht nur per Flieger!</p>
    <p class="intro__text">
      Bei uns findest Du Dein Hotel, Tickets für die Sehenswürdigkeiten und/oder das passende Event vor Ort.<br>
      Aus unserer grossen Angebotsvielfalt in über 40 Kategorien wie Gourmet- oder Fahrradreisen, Reiterferien<br>
      oder Yogareisen findest auch Du Deine nächste Auszeit vom Alltag. Wenn Du Dich inspirieren lassen möchtest,<br>
      dann blättere spontan in unserem eigens geschriebenen Reisemagazin mit netten Insidern und pfiffigen Sporttipps.<br>
      Und auch in Deiner Reisevorbereitung lassen wir Dich nicht allein. Damit Du ganz unbeschwert zu Deinen<br>
      Reisezielen kommst, findest Du dank einer Flug-, Hotel-, Mietwagen- und VISA Online Recherche Möglichkeit<br>
      auch ein Rundum-sorglos-Paket, dass selbstverständlich auch über unsere Partner buchbar ist.
    </p>
    <p class="intro__claim"><b>WEGFALKE</b> steht für <b>Liebe zum Detail</b> und <b>Qualität</b>.</p>
  </div>

  <ul class="offer">
    <li class="offer__item" style="left:852px;top:40px">
      <span class="offer__icon"><svg width="17" height="17" viewBox="0 0 24 24" fill="none" stroke="#fff" stroke-width="1.6"><circle cx="12" cy="12" r="9"/><path d="M3 12h18M12 3c3 3 3 15 0 18M12 3c-3 3-3 15 0 18"/></svg></span>
    </li>
    <li class="offer__item" style="left:862px;top:72px">
      <span class="offer__icon"><svg width="17" height="17" viewBox="0 0 24 24" fill="none" stroke="#fff" stroke-width="1.6"><path d="M12 3l2.7 5.6 6.1.9-4.4 4.3 1 6.1L12 17l-5.4 2.9 1-6.1-4.4-4.3 6.1-.9z"/></svg></span>
    </li>
    <li class="offer__item" style="left:866px;top:104px">
      <span class="offer__icon"><svg width="17" height="17" viewBox="0 0 24 24" fill="none" stroke="#fff" stroke-width="1.6"><circle cx="12" cy="12" r="9"/><path d="M12 4l2 8-2 8-2-8zM4 12l8-2 8 2-8 2z"/></svg></span>
    </li>
    <li class="offer__item" style="left:867px;top:136px">
      <span class="offer__icon"><svg width="17" height="17" viewBox="0 0 24 24" fill="none" stroke="#fff" stroke-width="1.6"><path d="M3 19V9M3 15h18v4M21 15v-3a2 2 0 0 0-2-2h-8v5"/><circle cx="7" cy="12" r="1.6"/></svg></span>
    </li>
    <li class="offer__item" style="left:865px;top:167px">
      <span class="offer__icon"><svg width="17" height="17" viewBox="0 0 24 24" fill="none" stroke="#fff" stroke-width="1.6"><path d="M20 4l-6 6-9-2-2 2 7 4-3 4H4l-1 1 4 1 1 4 1-1v-3l4-3 4 7 2-2-2-9 6-6c1-1 1-3 0-3s-2 0-3 1z"/></svg></span>
    </li>
    <li class="offer__item" style="left:862px;top:199px">
      <span class="offer__icon"><svg width="17" height="17" viewBox="0 0 24 24" fill="none" stroke="#fff" stroke-width="1.6"><rect x="3" y="5" width="18" height="16" rx="1"/><path d="M3 10h18M8 3v4M16 3v4M7 14h2M11 14h2M15 14h2M7 17h2M11 17h2"/></svg></span>
    </li>
    <li class="offer__item" style="left:852px;top:231px">
      <span class="offer__icon"><svg width="17" height="17" viewBox="0 0 24 24" fill="none" stroke="#fff" stroke-width="1.6"><path d="M4 16v-4l2-5h12l2 5v4zM4 12h16"/><circle cx="7.5" cy="14" r="1"/><circle cx="16.5" cy="14" r="1"/><path d="M6 16v2M18 16v2"/></svg></span>
    </li>
  </ul>

  <span class="offer__label" style="top:43px">Themenreisen</span>
  <span class="offer__label" style="top:75px">Aktivitäten</span>
  <span class="offer__label" style="top:107px">Touren</span>
  <span class="offer__label" style="top:138px">Hotels</span>
  <span class="offer__label" style="top:170px">Flüge</span>
  <span class="offer__label" style="top:202px">Events</span>
  <span class="offer__label" style="top:233px">Mietwagen</span>
</section>

<!-- Geschlossene Variante -->
<section class="closed photo photo--jetty-warm" role="img" aria-label="Foto: Steg zu Wasserbungalows im Sonnenuntergang über beide Panels">
  <span class="closed__fold"></span>
  <h2 class="headline" style="left:26px;top:64px">Wir sind<br>voller<br>Reise-<br>vielfalt</h2>
</section>

<p class="note">Flyer DIN lang 6 Seiten, Fensterfalz<br>links: geschlossene Variante</p>

</body>
</html>
```